Flyer for the Harvest of lanterns conference

Flyer design for an annual international conference called "MERIVAL 2017". This is a conference for young adults, so we hope to produce a design that is both professional and appealing to young people in general

We'd like the flyer to showcase the conference brand logo, and clearly highlight the key information to people who will read it.

Target Market(s)

Young people, young adults

Industry/Entity Type

Religious

Font styles to use
Sans Serif

Colors

Designer to choose colors to be used in the design.

Requirements
Must have
• - Should be only one page (Vertical or Horizontal).
• - the MERVAL logo and all the information found in the attached text file. This includes: Main topic: Your sons and daughters shall prophesy,
• Dates and time, location, contact information and everything that is in the attached text file.
Nice to have
• It would be nice to see samples where the white logo is used and another where the black one is used.
Should not have
• This is NOT a folded flyer, we will be sticking it on doors and public places. And we will be printing large simple to put on walls. So only one page with few words like an add (the words are in the attached file)

```html
<!DOCTYPE html>
<html lang="en">
<head>
<meta charset="utf-8">
<title>MERIVAL 2017 – Harvest of Lanterns Conference</title>
<link rel="stylesheet" href="https://fonts.googleapis.com/css2?family=Montserrat:wght@400;600;700;800&family=Questrial&display=swap">
<style>
  :root {
    --flame-deep: #c8240f;
    --flame-mid: #ef5a1c;
    --flame-glow: #ffd23a;
    --band-red: #a8200f;
    --band-dark: #7d1508;
    --ink: #111111;
    --maroon: #7a1a12;
    --white: #ffffff;
    --mist-top: #c9d6c4;
    --mist-mid: #e6e2a8;
    --mist-low: #b9cfd0;
  }
  * { margin: 0; padding: 0; box-sizing: border-box; }
  html, body { width: 927px; height: 1200px; overflow: hidden; background: #fff; }
  .flyer {
    position: relative;
    width: 927px; height: 1200px;
    font-family: "Montserrat", sans-serif;
    overflow: hidden;
  }
  .sky {
    position: absolute; left: 0; top: 0; width: 927px; height: 306px;
    background:
      radial-gradient(ellipse 360px 200px at 320px 250px, var(--flame-glow) 0%, #ffb02a 30%, transparent 75%),
      linear-gradient(180deg, var(--flame-deep) 0%, var(--flame-mid) 55%, #f7862a 100%);
  }
  .title-block {
    position: absolute; left: 120px; top: 48px; width: 480px; text-align: center;
  }
  .event-name { color: var(--white); font-weight: 700; font-size: 45px; letter-spacing: 2px; line-height: 1; }
  .event-theme { color: var(--ink); font-weight: 800; font-size: 35px; letter-spacing: 1px; margin-top: 16px; line-height: 1; }
  .event-type { color: var(--ink); font-weight: 400; font-size: 28px; letter-spacing: 1px; margin-top: 10px; line-height: 1; }
  .brand-mark {
    position: absolute; left: 615px; top: 33px; width: 196px; height: 162px;
    background: #0d0d0d;
    display: flex; flex-direction: column; align-items: center; justify-content: center; gap: 12px;
  }
  .brand-dot { width: 40px; height: 40px; border-radius: 50%; background: #e8a227; }
  .brand-name { color: #ffffff; font-weight: 700; font-size: 21px; letter-spacing: 1px; }
  .theme-band {
    position: absolute; left: 0; top: 306px; width: 927px; height: 154px;
    background: linear-gradient(180deg, var(--band-red), var(--band-dark));
    display: flex; align-items: center; justify-content: center; text-align: center;
  }
  .theme-text { color: var(--white); font-weight: 700; font-size: 43px; line-height: 1.28; letter-spacing: 1.5px; }
  .scene {
    position: absolute; left: 0; top: 460px; width: 927px; height: 645px;
    background:
      radial-gradient(ellipse 260px 200px at 150px 540px, rgba(240,190,60,.55), transparent 70%),
      radial-gradient(ellipse 420px 260px at 450px 200px, rgba(255,240,170,.8), transparent 75%),
      linear-gradient(180deg, var(--mist-top) 0%, var(--mist-mid) 40%, var(--mist-low) 100%);
  }
  .details { position: absolute; left: 0; top: 488px; width: 927px; text-align: center; }
  .dates { color: var(--maroon); font-weight: 800; font-size: 37px; letter-spacing: .5px; }
  .venue { color: var(--ink); font-weight: 800; font-size: 31px; letter-spacing: 1px; margin-top: 22px; }
  .hotel { color: var(--maroon); font-weight: 700; font-size: 24px; margin-top: 4px; }
  .address { font-family: "Questrial", sans-serif; color: var(--ink); font-size: 27px; line-height: 36px; margin-top: 4px; margin-left: -30px; }
  .speakers { position: absolute; left: 0; top: 897px; width: 927px; text-align: center; }
  .speakers-title { color: var(--maroon); font-weight: 700; font-size: 19px; margin-bottom: 4px; }
  .speakers-list { list-style: none; }
  .speakers-list li { color: var(--ink); font-weight: 700; font-size: 21px; line-height: 34px; }
  .speakers-list li::before { content: "• "; color: var(--maroon); }
  .contact-band {
    position: absolute; left: 0; top: 1105px; width: 927px; height: 95px;
    background: linear-gradient(180deg, var(--band-red), var(--band-dark));
    color: var(--white); text-align: center; font-family: "Questrial", sans-serif;
  }
  .contact-line { display: flex; justify-content: center; align-items: center; gap: 32px; margin-top: 14px; font-size: 24px; }
  .contact-item { display: flex; align-items: center; gap: 10px; }
  .web { font-size: 24px; letter-spacing: 4px; margin-top: 8px; }
</style>
</head>
<body>
<main class="flyer">
  <div class="sky" role="img" aria-label="Glowing sunset sky with bright clouds"></div>
  <header class="title-block">
    <h1 class="event-name">MERIVAL 2017</h1>
    <p class="event-theme">HARVEST OF LANTERNS</p>
    <p class="event-type">CONFERENCE</p>
  </header>
  <div class="brand-mark">
    <span class="brand-dot"></span>
    <span class="brand-name">MERVAL</span>
  </div>

  <section class="theme-band">
    <h2 class="theme-text">YOUR SONS AND DAUGHTERS<br>SHALL PROPHESY</h2>
  </section>

  <div class="scene" role="img" aria-label="Soft misty photo of a young person with raised arms in a field, blended with a faint face"></div>

  <section class="details">
    <p class="dates">1 - 2 - 3 SEPTEMBER 2017 | 6:00PM</p>
    <p class="venue">CEDARLINE BALLROOM</p>
    <p class="hotel">Harborview Lantern Inn</p>
    <p class="address">412 Harbor Road<br>Eastbrook, ME 04299 USA</p>
  </section>

  <section class="speakers">
    <p class="speakers-title">Speakers Include:</p>
    <ul class="speakers-list">
      <li>Prophet Lucien Mbaraka</li>
      <li>Bishop Samuel Ndolo</li>
      <li>Prophet Joel Amani Lukusa</li>
      <li>Prophet Remy Tshala</li>
      <li>Prophet Aaron Mbuyi</li>
    </ul>
  </section>

  <footer class="contact-band">
    <div class="contact-line">
      <span class="contact-item">
        <svg width="22" height="22" viewBox="0 0 24 24" fill="none" stroke="#fff" stroke-width="1.6"><circle cx="12" cy="12" r="10.5"/><path d="M9 6.5l1.6 3-1.3 1.3c.8 1.6 1.9 2.7 3.5 3.5l1.3-1.3 3 1.6-.8 2c-4.6-.2-8.3-3.9-8.5-8.5z"/></svg>
        +1 (207) 555 0148
      </span>
      <span class="contact-item">
        <svg width="24" height="20" viewBox="0 0 24 20" fill="none" stroke="#fff" stroke-width="1.6"><path d="M2 8 L12 2 L22 8 V18 H2 Z"/><path d="M2 8 L12 14 L22 8"/></svg>
        hello@lanternhall.org
      </span>
    </div>
    <p class="web">www.merivalconf.org</p>
  </footer>
</main>
</body>
</html>
```